Web design for new streaming audio service

We need a homepage design for a new streaming audio service. Our company is called Olvantra, and we’re basically Vidorama for Audiobooks, Stand-Up Comedy, Lectures, Language Learning, etc. Essentially like Tunelark for everything audio EXCEPT music.
You don’t have to code the homepage (Design Only), but it should include 3 different designs to work with 1) Web; 2) Phones; 3) Tablets.
Below is a link to a mockup of the web version which gives a good idea of what elements we want. This is just a mockup and we want you to improve it.
Once you download the mockup, please refer to the more detailed instructions below:
The following outlines the design project for the Olvantra homepage. We have provided a rough mockup of the homepage layout that gives you a general idea of what we’re going for. There are a few elements that we are attached to, and many others where you have complete creative freedom to do whatever you think looks good.
The ZIP file includes the following:
* Mockup to see what we have in mind (olvantra-homepage-mockup.jpg)
* Text used (olvantra-homepage-text.txt)
* Raw image of actor (olvantra-actor1.jpg)
* Raw images for samples (olvantra-sample-[name].jpg)
Although we have only provided a mockup layout for the web version, we also need you to provide a mobile phone and a tablet version of the design also. It’s very possible the tablet version may be substantially similar to the web version, but the mobile phone version will likely be much different.
All of the raw files are included in the attached ZIP file. Please use our photographs and text as provided although cropping, sizing, etc. is flexible per the instructions below.
Display Requirements:
* Web Version - Minimum resolution 1024x768 (72 dpi) but should look good on 1920x1080 (72 dpi) - Page should be designed to scale to look acceptable in all resolutions in between.
* Phone Version - Minimum Zentro 4 - 640x960 (326 dpi) but should look good on Korvel Nimbus Q5 - 1920x1080 (441 dpi) - Page should be designed to scale to look acceptable in all resolutions and devices in between.
* Tablet Version - Minimum Pagewick Ember LX 7” - 1280x800 (216 dpi) but should also look good on a Slato Breeze - 2048x1536 (264 dpi) - Page should be designed to scale to look acceptable in all resolutions and devices in between.
Above the Fold - We want to make sure the Olvantra logo, Member Login Link, Large Photo, Headline, Price, Button, and the first row of sample images are all “Above the fold”. As a general guideline, this means 600 pixels high on a 1024x768 72 dpi web screen. This requirement is less important on Phone versions.
Top Logo Bar - We want to retain the blue bar with the Olvantra logo on the page, although we are open to a different size, shape and positioning if it greatly enhances the design. Please use the standard logo color, although you are welcome to use either the horizontal or vertical orientation of the logo based on your design.
Text color, font and size - Feel free to design the text in anyway you choose as long as the text is readable on the target platforms.
Buttons - Feel free to use any size, shape and colors for the buttons as long as they are obvious and clickable relative to the page. The only exception is the Chatterly button should follow the Chatterly color scheme and logo treatment (the mockup doesn’t seem 100% correct.)
Top Photograph - We want to retain the large photograph across the top of the screen although final shape and dimensions are flexible.
Size and shape of content samples (i.e. Audiobooks, Stand-Up Comedy, etc.) - Feel free to design the content samples in anyway you choose.
Three Sales Points (i.e. Listen on your Zentro…, All you can enjoy…, etc.) - The Three Sales Points are envisioned to each have a corresponding illustration which you should provide and have rights for. The placeholder is represented by a square next to the text. The color size and shape of these elements are flexible and can be designed in any way you choose.
Opt-in form - Feel free to design the opt-in form in anyway you choose as long as the text is readable and the interactivity is obvious on the target platforms.
Text links and copyright notice - Feel free to design the bottom of the page text links and copyright notice in anyway you choose.
Additional colors, graphic design elements, etc. - Feel free to use any additional colors, graphic design elements, etc. to support your design.

```html
<!DOCTYPE html>
<html lang="en">
<head>
<meta charset="utf-8">
<title>Olvantra – Unlimited listening</title>
<link rel="stylesheet" href="https://fonts.googleapis.com/css2?family=Kalam:wght@400;700&family=Open+Sans:wght@400;600&display=swap">
<style>
:root{
  --sky:#5aa9d6;
  --sky-light:#8fd0f0;
  --rose:#e05a6a;
  --rose-soft:#e8a0a0;
  --coral:#f55a3c;
  --apricot:#f49a5a;
  --peach:#fbbf7a;
  --ink:#1e1e1e;
  --slate:#555555;
  --text-dark:#3a3a3a;
  --pink-text:#f36b80;
  --white:#ffffff;
  --chat-blue:#3b5998;
}
*{margin:0;padding:0;box-sizing:border-box}
html,body{width:953px;height:1200px;overflow:hidden;background:var(--white)}
body{position:relative;font-family:"Open Sans",Arial,sans-serif}
.hand{font-family:"Kalam",cursive}

.hero{position:absolute;left:0;top:0;width:953px;height:466px;overflow:hidden;
  background:linear-gradient(100deg,#f4f1ed 0%,#efe9e3 34%,#e2cbb7 48%,#c99a7a 62%,#b58466 74%,#8a7a72 86%,#5e6a80 100%)}
.hero-photo{position:absolute;inset:0;
  background:linear-gradient(180deg,rgba(255,255,255,0) 0%,rgba(255,255,255,0) 62%,rgba(92,104,128,.55) 100%)}

.topbar{position:absolute;left:0;top:26px;width:953px;height:58px;background:var(--sky)}
.nav a{position:absolute;top:38px;color:#22445a;font-size:13px;text-decoration:none;line-height:20px}
.nav .home{left:136px;top:0;width:48px;height:58px;background:var(--rose);color:var(--white);font-weight:600;text-align:center;padding-top:38px}
.member-login{position:absolute;left:744px;top:3px;color:var(--white);font-size:10px}
.brand{position:absolute;left:416px;top:30px;width:120px;text-align:center;color:var(--white);font-size:18px;line-height:22px;font-weight:600}

.headline{position:absolute;left:130px;top:124px;font-size:34px;line-height:40px;color:var(--text-dark);letter-spacing:1px;font-weight:400}
.price-badge{position:absolute;left:135px;top:192px;width:148px;height:148px;border-radius:50%;background:var(--sky-light);text-align:center;color:var(--white)}
.price-badge .price{margin-top:24px;font-size:16px;line-height:18px;font-weight:600}
.price-badge .cta{display:block;margin-top:8px;color:var(--ink);font-size:14px;text-decoration:underline;font-weight:600}
.price-badge .note{margin-top:10px;font-size:12px;line-height:15px}

.section-band{position:absolute;left:0;top:466px;width:953px;height:50px;background:var(--ink);text-align:center;color:var(--pink-text);font-size:22px;line-height:50px}
.section-band svg{vertical-align:middle;margin:0 8px}

.mosaic{position:absolute;left:0;top:516px;width:953px;height:462px}
.block{position:absolute}
.tile{position:absolute;overflow:hidden}
.tile .label{position:absolute;left:0;right:0;bottom:0;padding:6px 4px 8px;background:rgba(30,30,30,.55);color:var(--white);text-align:center;font-size:18px;line-height:22px}
.tile .label::before{content:"";display:block;width:10px;height:10px;margin:0 auto 4px;border-left:3px solid var(--white);border-top:3px solid var(--white);transform:rotate(45deg)}

.features{position:absolute;left:0;top:978px;width:953px;height:78px;background:var(--slate)}
.feature{position:absolute;top:9px;display:flex;align-items:center;gap:14px}
.feature p{color:var(--pink-text);font-size:14px;line-height:16px;font-style:italic}

.signup{position:absolute;left:0;top:1056px;width:953px;height:118px;background:var(--ink)}
.signup h2{position:absolute;left:130px;top:14px;color:var(--white);font-size:18px;font-weight:400;font-style:italic}
.signup .copy{position:absolute;left:130px;top:42px;width:210px;color:var(--white);font-size:10.5px;line-height:13px}
.signup .fine{position:absolute;left:130px;top:98px;color:var(--pink-text);font-size:10px}
.email-field{position:absolute;left:368px;top:18px;width:225px;height:24px;border:1px solid #cccccc;color:#999;font-size:12px;padding:3px 6px}
.btn-access{position:absolute;left:636px;top:18px;width:190px;height:26px;background:linear-gradient(#7a7a7a,#5a5a5a);color:var(--white);font-size:13px;text-align:center;line-height:26px;border:1px solid #888}
.btn-chatterly{position:absolute;left:636px;top:78px;width:190px;height:26px;background:var(--chat-blue);color:var(--white);font-size:13px;line-height:26px;display:flex;align-items:center;gap:8px;padding-left:6px}
.btn-chatterly .sq{width:16px;height:16px;background:var(--white)}
.or{position:absolute;left:722px;top:56px;color:var(--white);font-size:12px}

.legal{position:absolute;left:0;top:1174px;width:953px;height:26px;background:#2a2a2a;color:#aaaaaa;font-size:8px;line-height:26px}
.legal .copyright{position:absolute;left:130px}
.legal .links{position:absolute;left:330px;color:var(--white)}
</style>
</head>
<body>

<div class="hero">
  <div class="hero-photo" role="img" aria-label="Photo of a smiling young man wearing headphones, looking at his phone"></div>
</div>

<header class="topbar">
  <nav class="nav">
    <a class="home" href="#">Home</a>
    <a href="#" style="left:197px">About Us</a>
    <a href="#" style="left:271px">Celebrity Interviews</a>
    <a href="#" style="left:552px">Audiobooks</a>
    <a href="#" style="left:642px">Fitness Programs</a>
    <a href="#" style="left:764px">Contact</a>
  </nav>
  <span class="member-login">Member Login</span>
  <div class="brand">Olvantra</div>
</header>

<h1 class="headline hand">Unlimited listening.<br>&nbsp;Wherever you are.</h1>

<div class="price-badge">
  <p class="price">Only $9.99<br>per month</p>
  <a class="cta" href="#">Start Your Free Trail</a>
  <p class="note">Credit Card<br>Not Required</p>
</div>

<div class="section-band hand">
  <svg width="14" height="22" viewBox="0 0 14 22"><path d="M5 2v14" stroke="#f36b80" stroke-width="2"/><ellipse cx="3" cy="17" rx="3.5" ry="3" fill="#f36b80"/><path d="M5 2c4 2 6 4 5 8" stroke="#f36b80" stroke-width="2" fill="none"/></svg>
  What you can listen to on Olvantra
  <svg width="14" height="22" viewBox="0 0 14 22"><path d="M5 2v14" stroke="#f36b80" stroke-width="2"/><ellipse cx="3" cy="17" rx="3.5" ry="3" fill="#f36b80"/><path d="M5 2c4 2 6 4 5 8" stroke="#f36b80" stroke-width="2" fill="none"/></svg>
</div>

<section class="mosaic">
  <div class="block" style="left:0;top:0;width:128px;height:146px;background:var(--coral)"></div>
  <div class="block" style="left:0;top:146px;width:128px;height:186px;background:var(--peach)"></div>
  <div class="block" style="left:0;top:332px;width:128px;height:130px;background:var(--rose)"></div>
  <div class="block" style="left:128px;top:168px;width:119px;height:108px;background:var(--rose-soft)"></div>
  <div class="block" style="left:247px;top:0;width:121px;height:132px;background:var(--coral)"></div>
  <div class="block" style="left:503px;top:0;width:120px;height:132px;background:var(--rose)"></div>
  <div class="block" style="left:391px;top:132px;width:112px;height:144px;background:var(--apricot)"></div>
  <div class="block" style="left:623px;top:200px;width:201px;height:62px;background:var(--rose)"></div>
  <div class="block" style="left:824px;top:0;width:129px;height:178px;background:var(--coral)"></div>
  <div class="block" style="left:824px;top:178px;width:129px;height:126px;background:var(--apricot)"></div>
  <div class="block" style="left:824px;top:304px;width:129px;height:158px;background:var(--rose-soft)"></div>
  <div class="block" style="left:313px;top:276px;width:126px;height:186px;background:var(--peach)"></div>

  <div class="tile" role="img" aria-label="Language learning album cover" style="left:128px;top:0;width:119px;height:168px;background:linear-gradient(#1a1a2a,#1d8fd6 45%,#1d8fd6)"><div class="label">Language<br>Learning</div></div>
  <div class="tile" role="img" aria-label="Biography audiobook cover with author portrait" style="left:368px;top:0;width:135px;height:132px;background:linear-gradient(#7a6e60,#4a4038)"><div class="label">Biographies&amp;<br>Memoirs</div></div>
  <div class="tile" role="img" aria-label="Stand-up comedy album cover" style="left:623px;top:0;width:201px;height:200px;background:linear-gradient(135deg,#c9b79a,#8a6f58 60%,#3a3028)"><div class="label">Stand-Up<br>Comedy</div></div>
  <div class="tile" role="img" aria-label="Guided meditation album cover" style="left:247px;top:132px;width:144px;height:144px;background:linear-gradient(#b04aa8,#5a2a7a 60%,#2a1a3a)"><div class="label">Guided<br>Meditations</div></div>
  <div class="tile" role="img" aria-label="Fitness workout audio cover" style="left:503px;top:132px;width:120px;height:144px;background:linear-gradient(#f0f0e0,#4a6a7a 70%,#2a3a4a)"><div class="label">Fitness<br>Programs</div></div>
  <div class="tile" role="img" aria-label="Celebrity interview cover" style="left:128px;top:276px;width:185px;height:186px;background:linear-gradient(135deg,#d8c8a8,#3a2a22 60%,#1a1614)"><div class="label">Celebrity<br>Interview</div></div>
  <div class="tile" role="img" aria-label="Noir audiobook cover" style="left:439px;top:276px;width:184px;height:186px;background:linear-gradient(#1e2a2e,#4a5a5e 50%,#1a2224)"><div class="label">Audiobooks</div></div>
  <div class="tile" role="img" aria-label="Business training audio cover" style="left:623px;top:262px;width:201px;height:200px;background:linear-gradient(135deg,#a82a1a,#5a1a14 55%,#2a1a16)"><div class="label">Business<br>Trainings</div></div>
</section>

<section class="features">
  <div class="feature" style="left:130px">
    <svg width="38" height="60" viewBox="0 0 38 60"><rect x="4" y="2" width="30" height="56" rx="5" fill="#2a2a2a" stroke="#d9c48a" stroke-width="2"/><rect x="9" y="10" width="20" height="34" fill="#d9c48a"/><circle cx="19" cy="51" r="3" fill="#d9c48a"/></svg>
    <p class="hand">Listen on your Zentro,<br>Tabio or Robion<br>device</p>
  </div>
  <div class="feature" style="left:382px">
    <svg width="60" height="60" viewBox="0 0 60 60"><path d="M8 30 30 8h20v20L28 50z" fill="#d9c48a" transform="rotate(-10 30 30)"/><circle cx="42" cy="16" r="4" fill="#555"/><text x="26" y="36" font-size="16" fill="#555" font-family="Arial" transform="rotate(-10 30 30)">$</text></svg>
    <p class="hand">All you can enjoy for<br>one low monthly<br>price</p>
  </div>
  <div class="feature" style="left:658px">
    <svg width="60" height="60" viewBox="0 0 60 60"><circle cx="30" cy="30" r="24" fill="none" stroke="#d9c48a" stroke-width="6"/><path d="M13 13l34 34" stroke="#d9c48a" stroke-width="6"/></svg>
    <p class="hand">No obligation.<br>Cancel any<br>time</p>
  </div>
</section>

<section class="signup">
  <h2 class="hand">START YOUR FREE TRAIL</h2>
  <p class="copy">You will get instant &amp; unlimited access to all the material on olvantra for 14 days. There is no obligation &amp; you can cancel at any time.</p>
  <p class="fine">Credit Card Not Required For Free Trail</p>
  <div class="email-field">Your Email Address</div>
  <div class="btn-access">Get Instant Access</div>
  <span class="or">OR</span>
  <div class="btn-chatterly"><span class="sq"></span>Sign Up Using Chatterly</div>
</section>

<footer class="legal">
  <span class="copyright">©2014 Olvantra LLC.All Rights Reserved.</span>
  <span class="links">About | Help | Contact Us | Member Login | Privacy Policy | Terms of Service</span>
</footer>

</body>
</html>
```